Energy Management - layout ideas in Photoshop + $20 participation to 2nd & 3rd place

Dear Designers

• I am looking for an Graphic designer with web experience
• No Html or CSS coding will be required

$20 participation payments to second & third place designs !

This project is for a design theme we can use for our new web site @

http://www.kestrelwattgrid.co.uk/

Basically we like the homepage designs & "Providing the Results" slogan but I'm not quite happy using a template and require slight changes to make it look more bespoke & original .

I only require illustrations if you can come up with the layout as Photoshop, Vector, power point or similar formats we can use them when coding the site .
Inspiration & Similar web sites

http://www.pravolent.com/
http://www.dorvakt.com/
http://www.trasquilpower.com/
http://www.velmora-systems.com/
http://www.qz7gaugeportal.co.uk/
http://www.amber-crest.com/energy/
http://www.pivarenergy.com/solutions/overview
http://www.qtbxl.com/open-system-solutions/

Our other business http://www.daltrygauges.com/remote-meter-reading.html

we have many domains on our dedicated server and will require future help with designs & have more work for the right designer's

here are some examples of clients using our hosted service listed below

http://www.bramvolt-monitor.co.uk/

http://www.tindaleco-monitor.co.uk/

http://www.qnbe-monitor.co.uk/

http://www.orvalcore-monitor.co.uk/

http://www.zep-energy.com/

Reason: We have extended the design deadline due to lack of submissions

Reason: We have been unable to give this project our full attention until now Apologies Derek

Target Market(s)

People / Business's who are interested in very advanced Energy related products , saving money and reducing carbon emissions

Industry/Entity Type

Business

Requirements
Must have
• - Clean-professional look

"Providing the Results" slogan

Modern theme based around technology & wireless networking

must be based around the http://www.kestrelwattgrid.co.uk/ theme concept
Nice to have
• Would be nice to point out our Carbon Neutral web site and hosted services

```html
<!DOCTYPE html>
<html lang="en">
<head>
<meta charset="utf-8">
<title>KWG – Kestrel Watt Grid</title>
<link rel="stylesheet" href="https://fonts.googleapis.com/css2?family=Montserrat:wght@700&family=Open+Sans:wght@400;600&family=Arimo:wght@400;700&display=swap">
<style>
  :root{
    --page:#ebebeb;
    --navy:#1d2a78;
    --blue:#0a7fcf;
    --blue-deep:#0d55b5;
    --home:#1a1a1a;
    --products:#5a4320;
    --cases:#7d1233;
    --contact:#222222;
    --green:#1b7a10;
    --ink:#1e1e1e;
    --link:#0b79c8;
    --footer:#5d5d5d;
    --white:#ffffff;
    --dot:#555555;
    --dot-on:#d0401a;
  }
  *{box-sizing:border-box;margin:0;padding:0}
  html,body{width:1037px;height:1200px;overflow:hidden}
  body{background:var(--page);font-family:"Arimo",Arial,sans-serif;color:var(--ink);position:relative}
  a{text-decoration:none}
  .abs{position:absolute}
  .topline{left:0;top:0;width:1037px;height:4px;background:var(--blue-deep)}
  .login{left:802px;top:0;width:120px;height:26px;background:var(--blue-deep);color:var(--white);
    font:600 10px "Open Sans",sans-serif;display:flex;align-items:center;justify-content:center;gap:14px}
  .brand-card{left:118px;top:6px;width:196px;height:110px;background:var(--white);transform:rotate(-2deg);
    box-shadow:2px 4px 6px rgba(0,0,0,.25);display:flex;flex-direction:column;align-items:center;justify-content:center}
  .brand-name{font:700 38px "Montserrat",sans-serif;color:var(--navy);letter-spacing:1px;line-height:1}
  .brand-sub{font:700 8px "Montserrat",sans-serif;color:var(--navy);letter-spacing:.5px;margin-top:3px}
  .nav{left:400px;top:103px;height:39px;display:flex}
  .nav a{display:flex;align-items:center;justify-content:center;height:39px;color:var(--white);
    font:400 16px "Open Sans",sans-serif;margin-right:1px}
  .nav .home{width:80px;background:var(--home)}
  .nav .solutions{width:117px;background:var(--blue)}
  .nav .products{width:115px;background:var(--products)}
  .nav .cases{width:124px;background:var(--cases)}
  .nav .contact{width:115px;background:var(--contact);margin-right:0}
  .hero{left:101px;top:143px;width:856px;height:350px;border-top:3px solid var(--navy);
    background:
      radial-gradient(ellipse 180px 90px at 200px 300px,rgba(255,255,255,.75),rgba(255,255,255,0)),
      radial-gradient(ellipse 160px 70px at 370px 200px,rgba(255,255,255,.55),rgba(255,255,255,0)),
      radial-gradient(ellipse 120px 60px at 330px 330px,rgba(255,255,255,.6),rgba(255,255,255,0)),
      linear-gradient(200deg,#0e2a6a 0%,#1c4fa6 35%,#3d7fd0 60%,#7fb0e4 100%)}
  .hero-title{left:139px;top:184px;font:700 30px/48px "Montserrat",sans-serif;color:var(--white)}
  .hero-title span{display:block;background:var(--blue-deep);padding:0 14px}
  .hero-title .l1{width:228px}
  .hero-title .l2{width:487px}
  .hero-text{left:140px;top:297px;width:355px;font-size:13px;line-height:15.5px;color:#111}
  .btn{display:flex;align-items:center;justify-content:center;background:var(--green);color:var(--white);
    font-size:12px;border:1px solid #0f5209}
  .hero-btn{left:140px;top:392px;width:83px;height:30px}
  .thumb{top:374px;width:107px;height:107px;border:6px solid var(--white)}
  .t1{left:487px;background:radial-gradient(circle at 40% 30%,#a8a8a8,#5a5a5a 55%,#262626)}
  .t2{left:604px;background:radial-gradient(circle at 60% 65%,#d9c94a 0%,#8fae3c 25%,#2c7a55 55%,#1b5e3e)}
  .t3{left:722px;background:linear-gradient(170deg,#dfe7ef 0%,#b7c4d1 40%,#4a5a6c 60%,#2f3b4a)}
  .t4{left:836px;background:radial-gradient(circle at 70% 35%,#f3f1e2,#c9cfa8 30%,#6ea65a 60%,#2f7a2f)}
  .news{left:101px;top:509px;width:856px;height:32px;border:1px solid #b9b9b9;background:#f2f2f2;
    display:flex;align-items:center;padding-left:9px;font-size:11px}
  .news b{font-weight:400;color:#111;margin-right:14px}
  .news span{color:var(--link)}
  .col-title{top:559px;font:400 18px "Open Sans",sans-serif;color:#111}
  .col-img{top:588px;width:203px;height:95px}
  .img-about{left:101px;background:radial-gradient(ellipse 60px 80px at 120px 45px,#5a5a5a,#2a2a2a 60%,rgba(0,0,0,0)),linear-gradient(90deg,#050505,#1c1c1c 50%,#080808)}
  .img-what{left:318px;background:radial-gradient(ellipse 90px 30px at 50% 40%,#e7d34a,#c9467e 40%,rgba(0,0,0,0)),radial-gradient(circle at 50% 40%,#3d9fb8,#123a4d)}
  .img-prod{left:536px;background:radial-gradient(ellipse 70px 35px at 55% 60%,#f4f4f4,rgba(255,255,255,0)),linear-gradient(#4f6f98,#c9a998 55%,#8d6f5e)}
  .img-contact{left:755px;background:radial-gradient(ellipse 80px 30px at 50% 55%,rgba(240,140,50,.8),rgba(240,140,50,0)),linear-gradient(#2f8fd1,#7ec3ee)}
  .col-text{top:694px;width:203px;font-size:10.6px;line-height:12.6px;color:#111}
  .col-list{left:543px;top:694px;list-style:none;font-size:10.6px;line-height:16.3px}
  .col-list li{position:relative;padding-left:12px}
  .col-list li::before{content:"›";position:absolute;left:0;top:-2px;color:var(--cases);font-weight:700;font-size:14px}
  .col-btn{top:809px;width:84px;height:29px}
  .contact-row{left:756px;display:flex;gap:18px;font-size:10.6px;line-height:12.6px}
  .contact-row svg{flex:none;margin-top:1px}
  .contact-row a{color:var(--link)}
  .partners-title{left:101px;top:858px;font:400 18px "Open Sans",sans-serif;color:#111}
  .partners{left:101px;top:894px;width:856px;height:115px;background:var(--white)}
  .partner{top:936px;font:700 28px/34px "Arimo",sans-serif;transform:translateX(-50%);white-space:nowrap}
  .p1{left:168px;color:#0a7fcf}
  .p2{left:302px;color:#222;font-weight:400}
  .p3{left:472px;color:#c8102e;font-size:21px}
  .p4{left:657px;color:#0c4f96;font-size:34px}
  .p5{left:846px;color:#1a1a8a;font-size:26px}
  .dots{left:464px;top:1021px;display:flex;gap:6px}
  .dots i{width:10px;height:10px;border-radius:50%;background:var(--dot)}
  .dots i.on{background:var(--dot-on)}
  .footer{left:101px;top:1040px;width:856px;height:160px;background:var(--footer);border-top:3px solid var(--blue-deep)}
  .foot-links{top:1062px;list-style:none;font-size:11px;line-height:15.4px;color:var(--white)}
  .fl1{left:130px}.fl2{left:289px}
  .foot-brand{left:654px;top:1056px;color:var(--white)}
  .foot-brand .brand-name{color:var(--white);font-size:26px}
  .foot-brand .brand-sub{color:var(--white);font-size:6px;margin-top:2px}
  .foot-info{left:654px;top:1109px;font-size:10.4px;line-height:12.5px;color:var(--white);
    display:grid;grid-template-columns:66px 26px auto}
  .social{top:1163px;width:21px;height:21px;background:#2a5ea8;border:1px solid #1b3f73}
  .s1{left:654px}.s2{left:688px;background:#3a9ad8}.s3{left:724px;background:#1f6fa8}
  .copy{left:130px;top:1177px;font-size:9px;color:var(--white)}
</style>
</head>
<body>
  <div class="abs topline"></div>
  <div class="abs login">LOGIN
    <svg width="14" height="8" viewBox="0 0 14 8"><polyline points="1,7 7,1 13,7" fill="none" stroke="#fff" stroke-width="1.6"/></svg>
  </div>

  <div class="abs brand-card">
    <div class="brand-name">KWG</div>
    <div class="brand-sub">KESTREL WATT GRID</div>
  </div>

  <nav class="abs nav">
    <a class="home" href="#">HOME</a>
    <a class="solutions" href="#">SOLUTIONS</a>
    <a class="products" href="#">PRODUCTS</a>
    <a class="cases" href="#">CASE STUDIES</a>
    <a class="contact" href="#">CONTACT US</a>
  </nav>

  <div class="abs hero" role="img" aria-label="Electricity pylon against a blue cloudy sky"></div>
  <h1 class="abs hero-title"><span class="l1">PROVIDING</span><span class="l2">COMPLETE SOLUTIONS .....</span></h1>
  <p class="abs hero-text">Riusto odio dignissimos ducimus qui blanditiis praesentium voluptatum deleniti atque corrupti quos dolores et quas molestias excepturi sint occaecati cupiditate non provident, similique sunt in culpa qui officia deserunt mollitia animi, id est laborum et dolorum fuga.</p>
  <a class="abs btn hero-btn" href="#">Read More</a>
  <div class="abs thumb t1" role="img" aria-label="Steel pylon detail"></div>
  <div class="abs thumb t2" role="img" aria-label="Green gears and recycling symbol"></div>
  <div class="abs thumb t3" role="img" aria-label="Solar panel close-up"></div>
  <div class="abs thumb t4" role="img" aria-label="Hand holding an energy-saving bulb"></div>

  <div class="abs news"><b>LATEST NEWS :</b><span>Our Web servers provide constantly updated meter readings (from 1 minute to hourly readings) which can be viewed using a graphical interface.........</span></div>

  <h2 class="abs col-title" style="left:101px">About Us</h2>
  <h2 class="abs col-title" style="left:320px">What We Do</h2>
  <h2 class="abs col-title" style="left:538px">Products and Solutions</h2>
  <h2 class="abs col-title" style="left:755px">Contact Us Today</h2>

  <div class="abs col-img img-about" role="img" aria-label="Businessman in a dark suit"></div>
  <div class="abs col-img img-what" role="img" aria-label="Colourful energy lettering on a teal background"></div>
  <div class="abs col-img img-prod" role="img" aria-label="Hands joining puzzle pieces"></div>
  <div class="abs col-img img-contact" role="img" aria-label="Email, envelope and phone symbols on blue"></div>

  <p class="abs col-text" style="left:101px">Kestrel Watt Grid provides a web based application to gather data from Electricity Meters, Gas Meters, Water Meters, and other sources via GPRS or Ethernet modems storing the data on Web Servers and providing means by which customers can access their data via a web browser.</p>
  <p class="abs col-text" style="left:318px">We provide our own custom designed modems to collect the data, these modems automatically connect to the Web Server using GPRS or Ethernet, transmitting the data which is then stored on the server. The modems can handle meters with</p>
  <ul class="abs col-list">
    <li>Volt free pulse outputs</li>
    <li>IEC 62056 RS485 serial outputs</li>
    <li>Modbus RS485 serial outputs</li>
    <li>0-5V Analog signals from Temperature</li>
    <li>Wind Speed and Solar radiation sen-<br>sors.</li>
  </ul>

  <div class="abs contact-row" style="top:698px">
    <svg width="16" height="14" viewBox="0 0 16 14"><path d="M2 6 L8 2 L14 6 V13 H2 Z M2 6 L8 10 L14 6" fill="none" stroke="#222" stroke-width="1.3"/></svg>
    <span>No:218/40,<br>Autem quibusdam,<br>NY</span>
  </div>
  <div class="abs contact-row" style="top:748px">
    <svg width="16" height="14" viewBox="0 0 16 16"><path d="M3 1 L6 1 L7 5 L5 6.5 C6 9 7.5 10.5 9.5 11 L11 9 L15 10 L15 13 C15 14 14 15 13 15 C7 15 1 9 1 3 C1 2 2 1 3 1 Z" fill="#222"/></svg>
    <span>+44 161 555 0142</span>
  </div>
  <div class="abs contact-row" style="top:798px">
    <svg width="16" height="14" viewBox="0 0 16 16"><circle cx="8" cy="8" r="2.6" fill="none" stroke="#222" stroke-width="1.5"/><path d="M10.6 6 V9.5 C10.6 11 12.5 11.5 13.5 10 C15 7 13 2 8 2 C4 2 2 5 2 8 C2 12 5.5 14 9.5 13.5" fill="none" stroke="#222" stroke-width="1.5"/></svg>
    <a href="#">info@kwg.com</a>
  </div>

  <a class="abs btn col-btn" style="left:101px" href="#">Read More</a>
  <a class="abs btn col-btn" style="left:315px" href="#">Read More</a>
  <a class="abs btn col-btn" style="left:536px" href="#">Read More</a>

  <h2 class="abs partners-title">Our Partners</h2>
  <div class="abs partners"></div>
  <div class="abs partner p1">Dovrel</div>
  <div class="abs partner p2">Tarnline</div>
  <div class="abs partner p3">Railmark Lines</div>
  <div class="abs partner p4">Mivoro</div>
  <div class="abs partner p5">Brevon Tel</div>
  <div class="abs dots"><i></i><i class="on"></i><i></i><i></i><i></i></div>

  <footer class="abs footer"></footer>
  <ul class="abs foot-links fl1">
    <li>About Us</li><li>Management &amp; Board</li><li>Why Kestrel Watt Grid?</li><li>Certifications &amp; Awards</li><li>Advisory Board</li><li>Our Offices</li><li>Contact Us</li>
  </ul>
  <ul class="abs foot-links fl2" style="line-height:12.4px">
    <li>Solutions</li><li>Products</li><li>Case Studies</li><li>Demo Request</li><li>FAQ</li>
  </ul>
  <div class="abs foot-brand">
    <div class="brand-name">KWG</div>
    <div class="brand-sub">KESTREL WATT GRID</div>
  </div>
  <div class="abs foot-info">
    <span>Address</span><span>:</span><span>No:218/40, Autem quibusdam, NY</span>
    <span>Tel</span><span>:</span><span>+44 161 555 0142</span>
    <span>Fax</span><span>:</span><span>+44 870 555 0198</span>
    <span>Email</span><span>:</span><span>info@kwg.com</span>
  </div>
  <div class="abs social s1" role="img" aria-label="Social network link"></div>
  <div class="abs social s2" role="img" aria-label="Social network link"></div>
  <div class="abs social s3" role="img" aria-label="Social network link"></div>
  <p class="abs copy">© 2013 Kestrel Watt Grid. All Rights Reserved.</p>
</body>
</html>
```